The Marlow Method Diet Business Card

The Marlow Method is a revolutionary new diet approach. We need a fresh, different business card design for The Marlow Method. We would like the cards lettering and designed match with the color scheme of the logo(Orange,black,grey) and the website. We would like the front of the business card to be the pic of a scale(that people weigh themselves on).We have attached a pic we would like that kind of old school number scale. With the the words "want to lose weight?Eat what you crave! Change how it's made! Get moving! No gym required. Similar to our shirt design. At the Back of the card we would like our logo. My name Dwight Pemberly Jr. My telephone number 504-617-2254 my email dpemberlyjr@marlowmethod.example

Target Market(s)

Everyone who's looking to get into shape

Industry/Entity Type

Health And Wellness

Contact Information for Business Card

Name , company logo, weight scale. Want to have something people talk about that looks so refreshing

Colors
faa54b
f68d4d
000000
b2b2b2

Requirements
Must have
• Weight scale, logo and futuristic look. Nothing plain get creative baby!
Nice to have
• Something that would stand out in a crowd
Should not have
• Be boring or look like any other card or be anything like Brennick diet cards

```html
<!DOCTYPE html>
<html lang="en">
<head>
<meta charset="utf-8">
<title>The Marlow Method Diet Business Card</title>
<link rel="stylesheet" href="https://fonts.googleapis.com/css2?family=Open+Sans:wght@400;600;700&display=swap">
<style>
  :root {
    --orange-light: #faa54b;
    --orange-deep: #f68d4d;
    --black: #000000;
    --grey: #b2b2b2;
    --ink: #3a3a3a;
    --paper: #ffffff;
    --paper-shade: #f1f1f1;
    --backdrop: #e9e6e2;
  }
  * { box-sizing: border-box; margin: 0; padding: 0; }
  html, body { width: 1200px; height: 900px; overflow: hidden; }
  body {
    background: var(--backdrop);
    font-family: "Open Sans", Arial, sans-serif;
    position: relative;
  }
  .card {
    position: absolute;
    left: 260px;
    width: 680px;
    height: 389px;
    background: var(--paper);
    box-shadow: 0 6px 18px rgba(0,0,0,.18);
    overflow: hidden;
    display: flex;
    flex-direction: column;
  }
  .card--front { top: 40px; }
  .card--back { top: 470px; }

  .card__top {
    height: 176px;
    background: linear-gradient(180deg, var(--paper) 0%, var(--paper-shade) 100%);
    display: flex;
    align-items: center;
    justify-content: center;
    gap: 70px;
  }
  .card__divider {
    height: 10px;
    background: linear-gradient(180deg, #d8d8d8, #9a9a9a);
    border-top: 2px solid var(--paper);
    border-bottom: 2px solid #7d7d7d;
  }
  .card__bottom {
    flex: 1;
    background: linear-gradient(180deg, var(--orange-light) 0%, var(--orange-deep) 100%);
    color: var(--paper);
    display: flex;
    flex-direction: column;
    align-items: center;
    justify-content: center;
    text-align: center;
  }

  .scale-art {
    width: 150px;
    height: 138px;
    border-radius: 28px;
    background: linear-gradient(160deg, #6a6a6a 0%, #1e1e1e 100%);
  }

  .brand {
    display: flex;
    align-items: center;
    gap: 14px;
  }
  .brand__dot {
    width: 38px;
    height: 38px;
    border-radius: 50%;
    background: var(--orange-deep);
  }
  .brand__name {
    font-weight: 600;
    font-size: 38px;
    color: var(--ink);
    letter-spacing: .5px;
  }
  .card--back .brand__name { font-size: 44px; }

  .pitch__headline { font-weight: 700; font-size: 24px; margin-bottom: 10px; }
  .pitch__line { font-weight: 600; font-size: 19px; line-height: 1.45; }
  .pitch__sep { margin: 0 10px; }
  .pitch__web { font-weight: 700; font-size: 20px; margin-top: 8px; }

  .contact__name { font-weight: 700; font-size: 25px; margin-bottom: 18px; }
  .contact__row {
    display: flex;
    align-items: center;
    gap: 8px;
    font-size: 18px;
    font-weight: 600;
    line-height: 1.6;
  }
  .contact__icon { width: 16px; height: 16px; fill: var(--paper); }
</style>
</head>
<body>

  <section class="card card--front" aria-label="Business card front">
    <div class="card__top">
      <div class="scale-art" role="img" aria-label="Old-school dial bathroom weight scale"></div>
      <div class="brand">
        <span class="brand__dot"></span>
        <span class="brand__name">The Marlow Method</span>
      </div>
    </div>
    <div class="card__divider"></div>
    <div class="card__bottom pitch">
      <p class="pitch__headline">Want to lose weight?</p>
      <p class="pitch__line">Eat what you crave!<span class="pitch__sep">|</span>Change how it's made!</p>
      <p class="pitch__line">Get moving!<span class="pitch__sep">|</span>No gym required</p>
      <p class="pitch__web">Visit marlowmethod.example</p>
    </div>
  </section>

  <section class="card card--back" aria-label="Business card back">
    <div class="card__top">
      <div class="brand">
        <span class="brand__dot"></span>
        <span class="brand__name">The Marlow Method</span>
      </div>
    </div>
    <div class="card__divider"></div>
    <div class="card__bottom contact">
      <p class="contact__name">Dwight Pemberly Jr.</p>
      <p class="contact__row">
        <svg class="contact__icon" viewBox="0 0 24 24" aria-hidden="true"><path d="M6.6 10.8a15.1 15.1 0 0 0 6.6 6.6l2.2-2.2a1 1 0 0 1 1-.25 11.4 11.4 0 0 0 3.6.57 1 1 0 0 1 1 1V20a1 1 0 0 1-1 1A17 17 0 0 1 3 4a1 1 0 0 1 1-1h3.5a1 1 0 0 1 1 1c0 1.25.2 2.45.57 3.57a1 1 0 0 1-.25 1z"/></svg>
        504-617-2254
      </p>
      <p class="contact__row">
        <svg class="contact__icon" viewBox="0 0 24 24" aria-hidden="true"><path d="M2 5h20v14H2z" fill="none" stroke="#fff" stroke-width="2"/><path d="M2 5l10 8 10-8" fill="none" stroke="#fff" stroke-width="2"/></svg>
        dpemberlyjr@marlowmethod.example
      </p>
    </div>
  </section>

</body>
</html>
```